Dufresne Roofing

Want a professional looking business card

Industry/Entity Type

Business

Contact Information for Business Card

Marc Dufresne ( Owner) marc@dufresneroofing-example.com, www.dufresneroofing-example.com, Adress: 4217 County road 42 Wendover,ON K0A3M1

```html
<!DOCTYPE html>
<html lang="en">
<head>
<meta charset="utf-8">
<title>Dufresne Roofing – Business Card</title>
<link href="https://fonts.googleapis.com/css2?family=Roboto:wght@400;500;700&display=swap" rel="stylesheet">
<style>
  :root {
    --brand-blue: #1d4587;
    --brand-gray: #76787b;
    --card-white: #ffffff;
    --ink: #1e1e1e;
    --page-bg: #e9e9ec;
  }
  * { margin: 0; padding: 0; box-sizing: border-box; }
  html, body { width: 1200px; height: 900px; overflow: hidden; }
  body {
    background: var(--page-bg);
    font-family: "Roboto", Arial, sans-serif;
    display: flex;
    flex-direction: column;
    align-items: center;
    justify-content: center;
    gap: 46px;
  }
  .card {
    position: relative;
    width: 660px;
    height: 377px;
    background: var(--card-white);
    overflow: hidden;
    box-shadow: 0 6px 18px rgba(0,0,0,0.18);
  }
  .card-art { position: absolute; inset: 0; width: 100%; height: 100%; }
  .wordmark {
    position: absolute;
    display: flex;
    align-items: center;
    gap: 12px;
    color: var(--brand-blue);
    font-weight: 700;
    text-transform: uppercase;
    letter-spacing: 2px;
    white-space: nowrap;
  }
  .wordmark-square {
    width: 18px; height: 18px;
    background: var(--brand-blue);
    flex: none;
  }
  .card-back .wordmark {
    font-size: 40px;
    left: 50%; top: 44%;
    transform: translate(-50%, -50%);
  }
  .card-front .wordmark {
    font-size: 20px;
    letter-spacing: 1.5px;
    gap: 10px;
    left: 36px; top: 152px;
  }
  .card-front .wordmark-square { width: 13px; height: 13px; }
  .divider {
    position: absolute;
    left: 330px; top: 110px;
    width: 2px; height: 190px;
    background: linear-gradient(to bottom, rgba(29,69,135,0), var(--brand-blue) 30%, var(--brand-blue) 70%, rgba(29,69,135,0));
  }
  .contact {
    position: absolute;
    left: 360px; top: 118px;
    color: var(--ink);
    font-size: 14px;
    line-height: 1.45;
  }
  .contact-name {
    color: var(--brand-blue);
    font-size: 24px;
    font-weight: 700;
    line-height: 1.1;
  }
  .contact-role { font-size: 14px; margin-bottom: 12px; }
  .contact-address { margin-bottom: 8px; }
  .contact-line { display: flex; align-items: center; gap: 8px; }
  .contact-icon { width: 13px; height: 13px; flex: none; fill: var(--brand-blue); }
</style>
</head>
<body>

  <section class="card card-back" aria-label="Card back">
    <svg class="card-art" viewBox="0 0 660 377" preserveAspectRatio="none" aria-hidden="true">
      <path d="M380,0 L660,0 L660,150 Q560,40 380,0 Z" fill="var(--brand-gray)"/>
      <path d="M0,377 L0,345 Q360,330 660,240 L660,377 Z" fill="var(--brand-blue)"/>
    </svg>
    <div class="wordmark"><span class="wordmark-square"></span>Dufresne Roofing</div>
  </section>

  <section class="card card-front" aria-label="Card front">
    <svg class="card-art" viewBox="0 0 660 377" preserveAspectRatio="none" aria-hidden="true">
      <path d="M300,0 L660,0 L660,250 Q560,60 300,0 Z" fill="var(--brand-blue)"/>
      <path d="M0,250 Q160,345 470,377 L0,377 Z" fill="var(--brand-gray)"/>
    </svg>
    <div class="wordmark"><span class="wordmark-square"></span>Dufresne Roofing</div>
    <div class="divider"></div>
    <div class="contact">
      <div class="contact-name">Marc Dufresne</div>
      <div class="contact-role">Owner</div>
      <div class="contact-address">4217 County road 42<br>Wendover,ON K0A3M1</div>
      <div class="contact-line">
        <svg class="contact-icon" viewBox="0 0 24 24"><path d="M6.6 10.8a15.1 15.1 0 0 0 6.6 6.6l2.2-2.2c.3-.3.7-.4 1-.2 1.1.4 2.3.6 3.600.6.6 0 1 .4 1 1V20c0 .6-.4 1-1 1A17 17 0 0 1 3 4c0-.6.4-1 1-1h3.5c.6 0 1 .4 1 1 0 1.3.2 2.5.6 3.6.1.3 0 .7-.2 1z"/></svg>
        (613) 555-0142
      </div>
      <div class="contact-line">
        <svg class="contact-icon" viewBox="0 0 24 24"><path d="M2 5h20v14H2z M4 7v.5l8 5 8-5V7z" fill-rule="evenodd"/></svg>
        marc@dufresneroofing-example.com
      </div>
      <div class="contact-line">
        <svg class="contact-icon" viewBox="0 0 24 24"><circle cx="12" cy="12" r="10"/><path d="M2 12h20M12 2c3 3 3 17 0 20M12 2c-3 3-3 17 0 20" stroke="#fff" stroke-width="1.5" fill="none"/></svg>
        www.dufresneroofing-example.com
      </div>
    </div>
  </section>

</body>
</html>
```